Design a Shirt Hang Tag for a brand new streetwear company

We need a hang tag for our apparel. This will be attached and shipper with every shirt, hat, and hoodie. We make streetwear/urban apparel. For a feel of our products see http://loomferal.co

We'd like to see something die cut with a shape that isn't a rectangle.
Looking for a design that embodies "Savage". We are looking for something bold and fun. Our colors usually consist of black. white, and red, but if you feel like doing something else that you feel could fit our brand,go for it. Were savage, we don't want normal.

Target Market(s)

inner city, age 13-29, multi-cultural

Industry/Entity Type

Clothing

Font styles to use
Sans Serif
Other font styles liked:
• artist's choice

Colors
ec1f27
ffffff
000000

Requirements
Must have
• site url: www.loomferal.co
• Band Name: Loom Feral
• Double sided tag
• Die cut design

```html
<!DOCTYPE html>
<html lang="en">
<head>
<meta charset="utf-8">
<title>Loom Feral Hang Tag</title>
<link rel="stylesheet" href="https://fonts.googleapis.com/css2?family=Oswald:wght@600&family=Great+Vibes&display=swap">
<style>
  :root {
    --brand-red: #e52129;
    --ink: #000000;
    --paper: #ffffff;
    --gold-dark: #c27a24;
    --gold-mid: #d89a3a;
    --gold-light: #f8e79a;
    --shadow: #c9c9c9;
    --mark-grey: #d4d4d6;
  }
  * { margin: 0; padding: 0; box-sizing: border-box; }
  html, body { width: 1200px; height: 1000px; overflow: hidden; background: var(--paper); }
  .canvas { position: relative; width: 1200px; height: 1000px; overflow: hidden; background: var(--paper); }

  .tag-art { position: absolute; }
  .tag-front .tag-art {
    left: 470px; top: 170px; width: 620px; height: 260px;
    transform: rotate(-38deg);
    border-radius: 40px 160px 180px 40px;
    background: linear-gradient(90deg, var(--paper) 0%, var(--paper) 52%, var(--ink) 52%, var(--ink) 58%, var(--brand-red) 58%);
    border: 6px solid var(--ink);
    box-shadow: 6px 6px 0 var(--shadow);
  }
  .tag-back .tag-art {
    left: 110px; top: 570px; width: 640px; height: 250px;
    transform: rotate(38deg);
    border-radius: 180px 40px 40px 160px;
    background: linear-gradient(100deg, var(--gold-dark), var(--gold-light) 22%, var(--gold-mid) 45%, var(--gold-light) 70%, var(--gold-dark) 88%, var(--gold-mid));
    box-shadow: -5px 6px 0 var(--shadow);
  }

  .tag-url {
    position: absolute; left: 505px; top: 375px;
    transform-origin: 0 50%;
    transform: rotate(-38deg);
    font-family: "Great Vibes", cursive;
    font-size: 38px; line-height: 1; color: var(--brand-red); white-space: nowrap;
  }

  .tag-name {
    position: absolute;
    font-family: "Oswald", sans-serif; font-weight: 600;
    text-transform: uppercase; white-space: nowrap; line-height: 1;
    text-align: center;
  }
  .tag-front .tag-name {
    left: 855px; top: 185px; width: 200px;
    font-size: 44px; color: var(--paper);
    transform: rotate(38deg);
  }
  .tag-back .tag-name {
    left: 210px; top: 580px; width: 240px;
    font-size: 50px; color: var(--brand-red);
    transform: rotate(-25deg);
  }
  .tag-name span { display: block; }

  .brand-signoff {
    position: absolute; left: 930px; top: 866px; width: 240px;
    font-family: "Oswald", sans-serif; font-weight: 600;
    font-size: 52px; line-height: 1; color: var(--mark-grey);
    text-transform: uppercase; text-align: center; white-space: nowrap;
  }
  .brand-signoff span { display: block; }
</style>
</head>
<body>
<main class="canvas">
  <section class="tag tag-back">
    <div class="tag-art" role="img" aria-label="Gold foil die-cut hang tag shaped like a pistol with swirling flame wings"></div>
    <p class="tag-name"><span>Loom</span><span>Feral</span></p>
  </section>

  <section class="tag tag-front">
    <div class="tag-art" role="img" aria-label="Black, white and red die-cut hang tag shaped like a pistol with red flame wings"></div>
    <p class="tag-url">www.loomferal.co</p>
    <p class="tag-name"><span>Loom</span><span>Feral</span></p>
  </section>

  <p class="brand-signoff"><span>Loom</span><span>Feral</span></p>
</main>
</body>
</html>
```